Banner Ad Design Project

We I need three call to action buttons for my new web site. The site is a medical supply company. that should equal 1030x280. The site buttons should say:

1- "EVERYDAY FREE SHIPPING on orders over $50. No code. No hassle."
2- "Call us for FREE EXPERT ADVICE. Click to learn more."
3- "Learn about our QTZ Program. Click to continue"

The site is pelvorantik.com, I need them to replace the flash banner on the home page. I have proper placement, but need them to be distinct colors so they get noticed.

Thank you!

```html
<!DOCTYPE html>
<html lang="en">
<head>
<meta charset="utf-8">
<title>Pelvorantik – Medical Supplies</title>
<link rel="stylesheet" href="https://fonts.googleapis.com/css2?family=Arimo:wght@400;700&family=Oswald:wght@600;700&family=Alegreya:ital,wght@1,500;1,700&display=swap">
<style>
:root{
  --page-bg:#f2f2f2;
  --column:#ffffff;
  --ink:#222222;
  --muted:#8a8a8a;
  --link:#1a8fd8;
  --line:#dcdcdc;
  --bar-top:#1fa0ea;
  --bar-bottom:#0c6fc7;
  --green-top:#9fe0ac;
  --green-bottom:#28a554;
  --yellow-top:#fbe97a;
  --yellow-bottom:#e7b416;
  --blue-top:#32c0ef;
  --blue-bottom:#0977cc;
  --accent-yellow:#ffe438;
  --btn-dark:#3a3a3a;
}
*{box-sizing:border-box;margin:0;padding:0}
html,body{width:1200px;height:762px;overflow:hidden}
body{background:var(--page-bg);font-family:"Arimo",Arial,sans-serif;color:var(--ink);position:relative}
.column{position:absolute;left:108px;top:0;width:967px;height:762px;background:var(--column)}
.abs{position:absolute}

/* account bar */
.account-bar{left:118px;top:9px;width:957px;height:32px;border:1px solid #e3e3e3;border-radius:3px;background:linear-gradient(#fafafa,#ececec)}
.account-links{right:16px;top:3px;display:flex;gap:2px}
.account-link{display:flex;align-items:center;gap:6px;height:24px;padding:0 9px;border:1px solid #d8d8d8;background:#f7f7f7;font-size:11px;font-weight:700;color:var(--muted)}

/* header */
.brand{left:110px;top:72px;display:flex;align-items:center;gap:10px}
.brand-mark{width:40px;height:40px;background:var(--ink)}
.brand-name{font-size:42px;font-weight:700;color:var(--ink);letter-spacing:-1px}
.help-banner{left:700px;top:68px;width:375px;height:55px;background:linear-gradient(#1b7fd9,#0b4fa8);display:flex;align-items:center}
.help-photo{width:46px;height:55px;background:linear-gradient(#e9c9a8,#6f4a33)}
.help-ask{font-family:"Alegreya",Georgia,serif;font-style:italic;color:#fff;font-size:20px;line-height:22px;margin-left:22px}
.help-call{font-family:"Alegreya",Georgia,serif;font-style:italic;font-weight:700;color:var(--accent-yellow);font-size:23px;line-height:25px;margin-left:18px;text-align:center}

/* search */
.search-bar{left:110px;top:125px;width:965px;height:55px;background:linear-gradient(var(--bar-top),var(--bar-bottom));border-radius:6px 6px 0 0}
.search-label{right:364px;top:14px;color:#fff;font-size:21px}
.search-input{right:52px;top:5px;width:300px;height:36px;background:#fff;border-radius:3px;font-size:11px;color:#999;padding:12px 16px}
.search-btn{right:8px;top:5px;width:38px;height:36px;background:#0d5fb4;border-radius:3px;display:flex;align-items:center;justify-content:center}

/* categories */
.categories{left:109px;top:206px;display:flex}
.category{width:96.6px;height:112px;position:relative}
.category-tile{position:absolute;left:0;right:0;top:33px;bottom:0;background:linear-gradient(#fff,#f1f1f1);border:1px solid var(--line);border-right:none}
.category:last-child .category-tile{border-right:1px solid var(--line)}
.category-icon{position:absolute;left:22px;top:2px;width:54px;height:58px;border-radius:6px;background:linear-gradient(#cfd3d8,#7d848c)}
.category-name{position:absolute;left:4px;right:4px;top:70px;text-align:center;font-size:11.5px;font-weight:700;text-decoration:underline;line-height:15px}

/* promo banners */
.promo{top:328px;width:291px;height:241px;border-radius:12px;overflow:hidden;box-shadow:0 8px 6px -4px rgba(0,0,0,.35)}
.promo-shipping{left:133px;background:linear-gradient(var(--green-top),var(--green-bottom))}
.promo-advice{left:447px;background:linear-gradient(var(--yellow-top),var(--yellow-bottom))}
.promo-program{left:761px;background:linear-gradient(var(--blue-top),var(--blue-bottom))}
.promo-title{font-family:"Oswald",Impact,sans-serif;font-weight:700;color:#fff;text-transform:uppercase;line-height:34px;font-size:33px;text-shadow:0 2px 3px rgba(0,0,0,.3);white-space:nowrap}
.promo-title.mixed{text-transform:none}
.promo-title.small{font-size:27px;letter-spacing:-.2px}
.hl{color:var(--accent-yellow)}
.promo-note{color:#fff;font-size:14px}
.promo-tag{font-family:"Oswald",Impact,sans-serif;font-weight:600;color:var(--accent-yellow);font-size:22px;line-height:25px}
.promo-art{border-radius:6px}
.pill{font-family:"Oswald",Impact,sans-serif;font-weight:600;color:#fff;font-size:19px;line-height:22px;border:3px solid #fff;border-radius:14px;text-shadow:0 1px 2px rgba(0,0,0,.35);display:flex;align-items:center;justify-content:center;text-align:center}

/* bottom row */
.cart-box{left:146px;top:592px;width:216px;height:107px;border:1px solid #e2e2e2}
.cart-head{height:42px;border-bottom:1px solid #e2e2e2;display:flex;align-items:center;gap:12px;padding-left:10px;font-size:13px;font-weight:700;background:linear-gradient(#fff,#f5f5f5)}
.cart-icon{width:24px;height:24px;background:#1670c4;border-radius:2px;display:flex;align-items:center;justify-content:center}
.cart-empty{font-size:11.5px;line-height:15px;padding:19px 0 0 20px}
.cart-empty b{color:#1a5fa8}
.product{top:592px;width:216px;height:144px;border:1px solid #d6d6d6;background:linear-gradient(#fff,#f6f6f6)}
.product-name{position:absolute;left:6px;right:6px;top:10px;text-align:center;font-size:13px;font-weight:400;line-height:16px;color:var(--link)}
.product-photo{position:absolute;left:58px;top:46px;width:90px;height:80px;border-radius:4px;background:linear-gradient(#e4e4e4,#8b8b8b)}
.buy-now{position:absolute;right:9px;bottom:9px;width:86px;height:29px;background:var(--btn-dark);border-radius:2px;color:#fff;font-size:13px;font-weight:700;display:flex;align-items:center;justify-content:center}
</style>
</head>
<body>
<div class="column"></div>

<header>
  <div class="abs account-bar">
    <nav class="abs account-links">
      <span class="account-link"><svg width="14" height="14" viewBox="0 0 14 14"><circle cx="7" cy="4.5" r="3.3" fill="#555"/><path d="M1 14c0-4 2.7-6 6-6s6 2 6 6z" fill="#2a6fc0"/></svg>My Account</span>
      <span class="account-link"><svg width="16" height="14" viewBox="0 0 16 14"><path d="M1 1h3l2 8h8l1.5-6H5" fill="none" stroke="#666" stroke-width="1.5"/><circle cx="7" cy="12" r="1.3" fill="#666"/><circle cx="13" cy="12" r="1.3" fill="#666"/></svg>My Cart</span>
      <span class="account-link"><svg width="16" height="14" viewBox="0 0 16 14"><path d="M1 1h3l2 8h8l1.5-6H5" fill="none" stroke="#666" stroke-width="1.5"/><circle cx="7" cy="12" r="1.3" fill="#666"/><circle cx="13" cy="12" r="1.3" fill="#666"/></svg>Checkout</span>
    </nav>
  </div>

  <div class="abs brand"><span class="brand-mark"></span><span class="brand-name">Pelvorantik</span></div>

  <div class="abs help-banner">
    <div class="help-photo" role="img" aria-label="Photo of a smiling support agent wearing a headset"></div>
    <div class="help-ask">Questions?<br>Need Help?</div>
    <div class="help-call">Call Us At:<br>(555) 014-2287</div>
  </div>

  <div class="abs search-bar">
    <span class="abs search-label">Search:</span>
    <span class="abs search-input">Search entire store here...</span>
    <span class="abs search-btn"><svg width="16" height="16" viewBox="0 0 16 16"><circle cx="6.5" cy="6.5" r="4.5" fill="none" stroke="#fff" stroke-width="2.2"/><path d="M10 10l4 4" stroke="#fff" stroke-width="2.5" stroke-linecap="round"/></svg></span>
  </div>
</header>

<nav class="abs categories">
  <div class="category"><div class="category-tile"></div><div class="category-icon" role="img" aria-label="Folding walker"></div><span class="category-name">Walkers and Rollators</span></div>
  <div class="category"><div class="category-tile"></div><div class="category-icon" role="img" aria-label="Toilet safety frame"></div><span class="category-name">Bathroom Equipment</span></div>
  <div class="category"><div class="category-tile"></div><div class="category-icon" role="img" aria-label="Pair of crutches"></div><span class="category-name">Canes and Crutches</span></div>
  <div class="category"><div class="category-tile"></div><div class="category-icon" role="img" aria-label="Wheelchair"></div><span class="category-name">Standard and Power Wheelchairs</span></div>
  <div class="category"><div class="category-tile"></div><div class="category-icon" role="img" aria-label="Medical stool"></div><span class="category-name">Furniture and Supplies</span></div>
  <div class="category"><div class="category-tile"></div><div class="category-icon" role="img" aria-label="Blue exam gloves" style="background:linear-gradient(#6fb0f2,#1e5fc4)"></div><span class="category-name">Gloves and Masks</span></div>
  <div class="category"><div class="category-tile"></div><div class="category-icon" role="img" aria-label="Absorbent underpad" style="background:linear-gradient(#d8ecfb,#8cc6ef)"></div><span class="category-name">Incontinence</span></div>
  <div class="category"><div class="category-tile"></div><div class="category-icon" role="img" aria-label="Hospital bed" style="background:linear-gradient(#a88064,#5a3522)"></div><span class="category-name">Beds and Mattresses</span></div>
  <div class="category"><div class="category-tile"></div><div class="category-icon" role="img" aria-label="Pedal exerciser"></div><span class="category-name">Personal Care</span></div>
  <div class="category"><div class="category-tile"></div><span class="category-name">More Categories</span></div>
</nav>

<section class="promos">
  <a class="abs promo promo-shipping">
    <div class="abs promo-title" style="left:21px;top:22px">Everyday <span class="hl">Free</span><br>Shipping!</div>
    <div class="abs promo-note" style="left:25px;top:92px">on orders over $50</div>
    <div class="abs promo-art" style="left:154px;top:104px;width:122px;height:110px;background:linear-gradient(#f2c65a,#a8741c)" role="img" aria-label="Cardboard shipping box"></div>
    <div class="abs promo-tag" style="left:21px;top:155px">No code.<br>No hassle.</div>
  </a>

  <a class="abs promo promo-advice">
    <svg class="abs" style="left:27px;top:18px" width="58" height="34" viewBox="0 0 58 34"><path d="M4 14c0-9 50-9 50 0v4H42v-5H16v5H4z" fill="#fff"/><rect x="12" y="18" width="34" height="14" rx="3" fill="#fff"/><circle cx="29" cy="25" r="4" fill="#e8b41a"/></svg>
    <div class="abs promo-title mixed" style="right:32px;top:17px">Call us for</div>
    <div class="abs promo-title small" style="left:17px;top:53px"><span class="hl">FREE</span> EXPERT ADVICE</div>
    <div class="abs promo-art" style="left:115px;top:92px;width:174px;height:149px;background:linear-gradient(#f7e6b0,#4f86c0)" role="img" aria-label="Photo of a nurse and a doctor"></div>
    <div class="abs pill" style="left:16px;top:146px;width:128px;height:78px;background:linear-gradient(#68d08a,#2aa552)">Click to learn<br>more...</div>
  </a>

  <a class="abs promo promo-program">
    <div class="abs promo-title" style="left:23px;top:22px">Learn about our<br><span class="hl">QTZ</span> Program</div>
    <div class="abs promo-art" style="left:99px;top:98px;width:100px;height:72px;background:linear-gradient(#c4d4de,#3d4650)" role="img" aria-label="Film strip graphic"></div>
    <div class="abs pill" style="left:43px;top:154px;width:209px;height:56px;background:linear-gradient(#ffd84a,#e2a00c)">Click to continue.</div>
  </a>
</section>

<aside class="abs cart-box">
  <div class="cart-head"><span class="cart-icon"><svg width="16" height="14" viewBox="0 0 16 14"><path d="M1 1h3l2 8h8l1.5-6H5" fill="none" stroke="#fff" stroke-width="1.5"/><circle cx="7" cy="12" r="1.3" fill="#fff"/><circle cx="13" cy="12" r="1.3" fill="#fff"/></svg></span>MY CART</div>
  <p class="cart-empty">You have <b>no items</b> in your<br>shopping cart.</p>
</aside>

<article class="abs product" style="left:372px">
  <h3 class="product-name">Exercise Peddler with<br>Attractive Silver Vein Finish</h3>
  <div class="product-photo" role="img" aria-label="Pedal exerciser"></div>
  <span class="buy-now">Buy Now!</span>
</article>
<article class="abs product" style="left:597px">
  <h3 class="product-name">Steerable Knee Walker</h3>
  <div class="product-photo" role="img" aria-label="Knee walker scooter"></div>
  <span class="buy-now">Buy Now!</span>
</article>
<article class="abs product" style="left:822px">
  <h3 class="product-name">Adjustable Height Home Bed<br>Assist Handle</h3>
  <div class="product-photo" role="img" aria-label="Bed assist handle"></div>
  <span class="buy-now">Buy Now!</span>
</article>
</body>
</html>
```